SEO AND WEB DESIGN COMPANY BUSINESS CARD DESIGN

I need an eye catching , simple business card design that will match my logo . I need 2 versions of it ( white background and black background) - SOME PEOPLE DID NOT GET IT AND SENDING US FRONT WHITE BACK WHITE VERSIONS WHICH IS NOT CORRECT.

ONE VERSION SHOULD BE BACK AND FRONT ALL BLACK , SECOND VERSION SHOULD BE BACK AND FRONT ALL WHITE

logo psd files are attached for both versions. The business card is going to have : First Name- Last name - position - phone numbers

```html
<!DOCTYPE html>
<html lang="en">
<head>
<meta charset="utf-8">
<title>Brightlane – Business Cards</title>
<link href="https://fonts.googleapis.com/css2?family=Oswald:wght@500&family=Source+Sans+3:wght@400;600&display=swap" rel="stylesheet">
<style>
  :root {
    --bg: #e4e4e4;
    --card-dark: #0b0c0e;
    --card-light: #f3f3f3;
    --ink-dark: #111111;
    --ink-light: #ffffff;
    --brand-blue: #4f86c6;
    --shadow: 3px 4px 6px rgba(0,0,0,0.35);
  }
  * { margin: 0; padding: 0; box-sizing: border-box; }
  html, body { width: 1200px; height: 960px; overflow: hidden; }
  body {
    background: radial-gradient(ellipse at center, #eeeeee 0%, var(--bg) 70%);
    font-family: "Source Sans 3", "Myriad Pro", sans-serif;
    position: relative;
  }
  .card {
    position: absolute;
    width: 488px;
    height: 279px;
    box-shadow: var(--shadow);
    overflow: hidden;
  }
  .card--dark { background: var(--card-dark); color: var(--ink-light); }
  .card--light { background: var(--card-light); color: var(--ink-dark); }
  .card--front-dark { left: 90px; top: 178px; }
  .card--front-light { left: 626px; top: 178px; }
  .card--back-dark { left: 90px; top: 498px; }
  .card--back-light { left: 626px; top: 498px; }

  /* Front */
  .wordmark {
    position: absolute;
    left: 0; right: 0; top: 98px;
    text-align: center;
    font-family: "Oswald", sans-serif;
    font-weight: 500;
    font-size: 54px;
    line-height: 1;
    letter-spacing: 1px;
  }
  .tagline {
    position: absolute;
    left: 0; right: 0; top: 170px;
    text-align: center;
    font-family: "Oswald", sans-serif;
    font-weight: 500;
    font-size: 11px;
    letter-spacing: 7px;
  }
  .front-url {
    position: absolute;
    left: 0; right: 0; top: 231px;
    text-align: center;
    font-size: 13px;
    font-weight: 600;
    letter-spacing: 1.2px;
  }
  .front-url .domain { color: var(--brand-blue); }

  /* Back */
  .brand-disc {
    position: absolute;
    left: 40px; top: 60px;
    width: 150px; height: 150px;
    border-radius: 50%;
    border: 16px solid var(--brand-blue);
  }
  .contact {
    position: absolute;
    right: 34px; top: 66px;
    text-align: right;
    font-size: 13px;
    line-height: 16px;
  }
  .contact__name {
    color: var(--brand-blue);
    font-weight: 600;
    font-size: 17px;
    line-height: 20px;
  }
  .contact__title { margin-bottom: 46px; }
  .contact__address { margin-bottom: 6px; }
  .contact__line { display: flex; justify-content: flex-end; align-items: center; gap: 3px; }
  .contact__line svg { width: 11px; height: 11px; flex: none; }
</style>
</head>
<body>

  <section class="card card--dark card--front-dark">
    <div class="wordmark">BRIGHTLANE</div>
    <div class="tagline">DESIGN &amp; MARKETING</div>
    <div class="front-url"><span class="domain">brightlane</span>.ca</div>
  </section>

  <section class="card card--light card--front-light">
    <div class="wordmark">BRIGHTLANE</div>
    <div class="tagline">DESIGN &amp; MARKETING</div>
    <div class="front-url"><span class="domain">brightlane</span>.ca</div>
  </section>

  <section class="card card--dark card--back-dark">
    <div class="brand-disc" role="img" aria-label="Brightlane brand mark area"></div>
    <div class="contact">
      <div class="contact__name">Daniel Carter</div>
      <div class="contact__title">President</div>
      <div class="contact__address">#412 3380 Harbour St<br>Lakeview BC V2X 4K8</div>
      <div class="contact__line">(555) 318- 4207
        <svg viewBox="0 0 12 12"><path fill="#4f86c6" d="M2.5 1 4.3 3 3.5 4.3a7 7 0 0 0 4.2 4.2L9 7.7l2 1.8-1.3 1.5C5.6 10.8 1.2 6.4 1 2.3z"/></svg>
      </div>
      <div class="contact__line">daniel@brightlane.ca
        <svg viewBox="0 0 12 12"><rect x="1" y="2.5" width="10" height="7" fill="none" stroke="#4f86c6"/><path d="M1 2.5 6 7l5-4.5" fill="none" stroke="#4f86c6"/></svg>
      </div>
      <div class="contact__line">brightlane.ca
        <svg viewBox="0 0 12 12"><g fill="none" stroke="#4f86c6" stroke-width=".9"><circle cx="6" cy="6" r="5"/><ellipse cx="6" cy="6" rx="2.2" ry="5"/><path d="M1 6h10M2 3.5h8M2 8.5h8"/></g></svg>
      </div>
    </div>
  </section>

  <section class="card card--light card--back-light">
    <div class="brand-disc" role="img" aria-label="Brightlane brand mark area"></div>
    <div class="contact">
      <div class="contact__name">Daniel Carter</div>
      <div class="contact__title">President</div>
      <div class="contact__address">#412 3380 Harbour St<br>Lakeview BC V2X 4K8</div>
      <div class="contact__line">(555) 318- 4207
        <svg viewBox="0 0 12 12"><path fill="#4f86c6" d="M2.5 1 4.3 3 3.5 4.3a7 7 0 0 0 4.2 4.2L9 7.7l2 1.8-1.3 1.5C5.6 10.8 1.2 6.4 1 2.3z"/></svg>
      </div>
      <div class="contact__line">daniel@brightlane.ca
        <svg viewBox="0 0 12 12"><rect x="1" y="2.5" width="10" height="7" fill="none" stroke="#4f86c6"/><path d="M1 2.5 6 7l5-4.5" fill="none" stroke="#4f86c6"/></svg>
      </div>
      <div class="contact__line">brightlane.ca
        <svg viewBox="0 0 12 12"><g fill="none" stroke="#4f86c6" stroke-width=".9"><circle cx="6" cy="6" r="5"/><ellipse cx="6" cy="6" rx="2.2" ry="5"/><path d="M1 6h10M2 3.5h8M2 8.5h8"/></g></svg>
      </div>
    </div>
  </section>

</body>
</html>
```